Poster for Kirtan Music Event

Design (3) 24" x 36" Posters

I have provided a sample a friend did in Australia: ( Picture No. 4 )

Use all the text on sample poster except the replacement changes below.

Replace with the following text as this is for different location:
Replacement Text:

Every Friday Night 7:00pm-8:30pm
Halewai Stretch & Rhythm Loft
742 Mellory St Kealu

Free Kirtan Experience! or Free Event
Rohan Velu & Companions

Optional Text:

A evening of music, singing of spiritual mantras, and refreshments

Bring flowers, musical instruments, friends, or just come with an open heart.

Meditate on transcendental sounds that provide rest for the mind & heart"

An evening of music & singing of sacred mantra's

```html
<!DOCTYPE html>
<html lang="en">
<head>
<meta charset="utf-8">
<title>Free Kirtan Experience</title>
<link rel="stylesheet" href="https://fonts.googleapis.com/css2?family=Uncial+Antiqua&family=Alegreya:ital,wght@1,500&family=Josefin+Sans:wght@400&display=swap">
<style>
  :root {
    --violet-deep: #3a1a6e;
    --violet: #5a2a96;
    --violet-glow: #7a3fb8;
    --border-rose: #b0479a;
    --border-plum: #6d2b8c;
    --gold-line: #e3b04a;
    --banner-red: #c8323a;
    --banner-orange: #f0873a;
    --title-yellow: #f6d23a;
    --title-orange: #f7a637;
    --name-orange: #f26a33;
    --date-yellow: #f5b73c;
    --body-white: #f4eefa;
    --photo-edge: #58b8e8;
  }
  * { margin: 0; padding: 0; box-sizing: border-box; }
  html, body { width: 800px; height: 1200px; overflow: hidden; background: var(--violet-deep); }
  .poster {
    position: relative;
    width: 800px; height: 1200px;
    overflow: hidden;
    background: linear-gradient(160deg, var(--border-rose), var(--border-plum) 45%, var(--border-rose));
  }
  .frame {
    position: absolute; left: 40px; top: 40px; right: 40px; bottom: 40px;
    border: 2px solid var(--gold-line);
    background: radial-gradient(ellipse at 50% 62%, var(--violet-glow) 0%, var(--violet) 40%, var(--violet-deep) 100%);
  }
  .photo {
    position: absolute; left: 88px; top: 185px; width: 618px; height: 415px;
    border: 4px solid var(--photo-edge);
    background: linear-gradient(100deg, #d8d4cc 0%, #8a9cb0 30%, #6a5a48 55%, #c89a5a 75%, #3d5a3a 100%);
  }
  .banner { position: absolute; left: 28px; top: 22px; width: 744px; height: 210px; }
  .banner-text {
    position: absolute; left: 80px; top: 42px; width: 680px;
    font-family: "Uncial Antiqua", serif;
    transform: rotate(3deg);
    transform-origin: left top;
  }
  .banner-free { font-size: 56px; color: var(--title-yellow); line-height: 1; margin-left: 8px; text-shadow: 2px 2px 3px rgba(80,0,0,.6); }
  .banner-title { font-size: 51px; color: var(--title-orange); line-height: 1.3; margin-left: 22px; text-shadow: 2px 2px 3px rgba(80,0,0,.6); white-space: nowrap; }
  .host {
    position: absolute; left: 40px; right: 40px; top: 622px;
    text-align: center;
    font-family: "Uncial Antiqua", serif;
    font-weight: 400;
    font-size: 50px; line-height: 64px;
    color: var(--name-orange);
    text-shadow: 1px 2px 3px rgba(40,0,40,.5);
  }
  .details {
    position: absolute; left: 180px; top: 772px;
    font-family: "Alegreya", serif; font-style: italic; font-weight: 500;
    font-size: 30px; line-height: 40px;
    color: var(--date-yellow);
    white-space: nowrap;
    text-shadow: 1px 2px 3px rgba(40,0,40,.5);
  }
  .details .date { margin-left: 8px; }
  .blurb {
    position: absolute; left: 50px; right: 50px; top: 924px;
    text-align: center;
    font-family: "Josefin Sans", sans-serif;
    font-size: 19.5px; line-height: 24px;
    color: var(--body-white);
  }
  .blurb p { margin-bottom: 13px; }
</style>
</head>
<body>
<div class="poster">
  <div class="frame"></div>
  <div class="photo" role="img" aria-label="Photo of the musician singing into a microphone while playing acoustic guitar, devotional painting behind"></div>
  <svg class="banner" viewBox="0 0 744 210" aria-hidden="true">
    <defs>
      <linearGradient id="bannerFill" x1="0" y1="0" x2="1" y2="0">
        <stop offset="0" stop-color="#c8323a"/>
        <stop offset="0.55" stop-color="#f0873a"/>
        <stop offset="1" stop-color="#c8323a"/>
      </linearGradient>
    </defs>
    <path d="M8 22 C 200 2, 420 40, 736 30 L 722 190 C 520 205, 300 160, 30 196 L 44 110 Z"
          fill="url(#bannerFill)" stroke="#f6c15a" stroke-width="2"/>
  </svg>
  <div class="banner-text">
    <div class="banner-free">FREE</div>
    <div class="banner-title">KIRTAN EXPERIENCE!</div>
  </div>
  <h1 class="host">ROHAN VELU<br>&amp; COMPANIONS</h1>
  <div class="details">
    <div class="date">Every Friday Night 7:00pm-8:30pm</div>
    <div>Halewai Stretch &amp; Rhythm Loft</div>
    <div>742 Mellory St Kealu</div>
  </div>
  <div class="blurb">
    <p>An evening of music, singing of spiritual mantras, and refreshments</p>
    <p>Bring flowers, musical instruments, friends, or just come<br>with an open heart.</p>
    <p>Meditate on transcendental sounds that provide rest<br>for the mind &amp; heart”</p>
    <p>An evening of music &amp; singing of sacred mantra’s</p>
  </div>
</div>
</body>
</html>
```